Presentation Template for Copperline Ventures

We would like to have a template for our presentations since we have a new logo and want a new general image.

The new template should have as minimum Cover/Title Page, Bullets page and Regular page. We have a new logo and need the template to mach with it. For the bullets and regular page we want the design no take much part for including content, so we would like something that makes the slides look good but leaving most of room free for writing.

We would like the logo on the footer of the regular slides (not of course for the cover, dividers etc)

I'm attaching de logo here. Our logo colours are #b80016, #006ac6 and black

Thank you

Industry/Entity Type

It Company

Font styles to use
Other font styles liked:
• Maven Pro

Colors
ec1f27
0355a3
000000

Requirements
Must have
• Presentation template with Cover/Title Page, Bullets page and Regular page. Must match with our new logo.
• We would like the logo on the footer of the regular slides (not of course for the cover, dividers etc)
• Our logo colours are #b80016, #006ac6 and black
Nice to have
• Other type of slides, special bullets etc
Should not have
• I don't know

```html
<!DOCTYPE html>
<html lang="en">
<head>
<meta charset="utf-8">
<title>Copperline Ventures – Presentation Template</title>
<link href="https://fonts.googleapis.com/css2?family=Lato:wght@300;400;700;900&display=swap" rel="stylesheet">
<style>
:root{
  --red:#c10a1d;
  --red-dark:#9e0614;
  --blue:#0355a3;
  --ink:#222;
  --grey:#9a9a9a;
  --paper:#f7f7f7;
  --pink:#f3dadd;
}
*{margin:0;padding:0;box-sizing:border-box}
html,body{width:1200px;height:1166px;overflow:hidden;background:#000}
body{position:relative;font-family:'Lato',sans-serif}
.slide{position:absolute;width:384px;height:220px;background:var(--paper);overflow:hidden}
.c1{left:12px}.c2{left:408px}.c3{left:806px}
.r1{top:9px}.r2{top:239px}.r3{top:470px}.r4{top:702px}.r5{top:933px}

.brand{position:absolute;top:9px;right:10px;display:flex;align-items:center;gap:4px;color:var(--red);font:700 7.6px/1 'Lato',sans-serif;letter-spacing:.8px;text-transform:uppercase}
.brand .mark{width:14px;height:14px;background:var(--red)}
.brand.light{color:#fff}.brand.light .mark{background:#fff}
.page{position:absolute;right:8px;bottom:5px;width:13px;height:9px;background:var(--blue);color:#fff;font:700 4.5px/9px 'Lato',sans-serif;text-align:center}

.head{position:absolute;left:12px;top:12px;color:var(--red);font:700 10px/1 'Lato',sans-serif}
.head.bar::before{content:"";position:absolute;left:-10px;top:-4px;width:3px;height:18px;background:var(--red)}
.head.under::after{content:"";position:absolute;left:0;bottom:-5px;width:14px;height:1.5px;background:var(--red)}

.copy{position:absolute;color:var(--grey);font:400 4.6px/1.85 'Lato',sans-serif}
.copy.white{color:#fff}
.copy.justify{text-align:justify}
.sub{position:absolute;color:var(--red);font:700 6.2px/1 'Lato',sans-serif;text-transform:uppercase}
.ph{position:absolute}
</style>
</head>
<body>

<!-- 1 Cover -->
<section class="slide c1 r1">
  <div style="position:absolute;left:0;top:0;width:384px;height:163px;background:var(--red)"></div>
  <h1 style="position:absolute;left:0;top:66px;width:384px;text-align:center;color:#fff;font:400 19px/1 'Lato',sans-serif">Project Title Here</h1>
  <p style="position:absolute;left:80px;top:93px;width:224px;text-align:center;color:#fff;font:400 6px/1.7 'Lato',sans-serif">Subtext here&nbsp; Subtext here&nbsp; Subtext here&nbsp; Subtext here&nbsp; Subtext here Subtext here&nbsp; Subtext here&nbsp; Subtext here</p>
  <div class="brand" style="top:181px;right:auto;left:131px;font-size:9.5px;gap:5px"><span class="mark" style="width:18px;height:18px"></span><span>Copperline<br>Ventures</span></div>
</section>

<!-- 2 Welcome -->
<section class="slide c2 r1">
  <h2 class="head under">Welcome Message !</h2>
  <div class="brand"><span class="mark"></span><span>Copperline<br>Ventures</span></div>
  <div class="ph" role="img" aria-label="Employee portrait" style="left:161px;top:52px;width:61px;height:61px;border-radius:50%;background:radial-gradient(circle at 50% 40%,#8a8f96,#3a3e44);border:2px solid #fff;box-shadow:0 0 0 1px #ddd"></div>
  <p style="position:absolute;left:0;width:384px;top:118px;text-align:center;font:400 6.4px/1 'Lato',sans-serif;color:var(--ink)">EMPLOYEE NAME</p>
  <p style="position:absolute;left:0;width:384px;top:127px;text-align:center;font:400 5px/1 'Lato',sans-serif;color:var(--ink)">Company Name</p>
  <p class="copy" style="left:28px;top:139px;width:332px">Liquorice candy drops applicake apple pie cupcake brownie bear claw cake gingerbread cotton candy. Bear claw croissant apple pie. Croissant cake sweet puff wafer . Liquorice candy drops applicake apple pie cupcake brownie bear claw cake gingerbread cotton candy. Bear claw croissant apple pie. Croissant cake sweet puff wafer. Liquorice candy drops applicake apple pie cupcake brownie bear claw cake gingerbread cotton candy. Bear claw croissant apple pie.</p>
  <p class="copy" style="left:28px;top:181px;width:332px">Liquorice candy drops applicake apple pie cupcake brownie bear claw cake gingerbread cotton candy. Bear claw croissant apple pie. Croissant cake sweet puff wafer . Liquorice candy drops applicake</p>
  <div class="page">01</div>
</section>

<!-- 3 Employee -->
<section class="slide c3 r1">
  <div class="brand"><span class="mark"></span><span>Copperline<br>Ventures</span></div>
  <div class="ph" role="img" aria-label="Employee photo, man in grey suit" style="left:10px;top:30px;width:120px;height:190px;background:linear-gradient(180deg,#d9d9d9,#7c7f84 60%,#55585c)"></div>
  <h2 style="position:absolute;left:150px;top:56px;color:var(--red);font:700 8.5px/1 'Lato',sans-serif;padding-left:5px;border-left:1.5px solid var(--red)">Emplyoee Name</h2>
  <p style="position:absolute;left:156px;top:69px;color:var(--grey);font:400 5.2px/1 'Lato',sans-serif">Designation</p>
  <p class="copy" style="left:156px;top:88px;width:204px">Liquorice candy drops applicake apple pie cupcake brownie bear claw cake gingerbread cotton candy. Bear claw croissant apple pie. Croissant cake sweet puff wafer . Liquorice candy drops applicake apple pie cupcake brownie bear claw cake gingerbread cotton candy. Bear claw croissant apple pie. Croissant cake sweet puff wafer. Liquorice candy drops applicake apple pie cupcake brownie bear claw cake gingerbread cotton candy. Bear claw croissant apple pie.</p>
  <div style="position:absolute;left:93px;top:155px;width:265px;height:45px;background:var(--red)"></div>
  <p style="position:absolute;left:98px;top:161px;width:255px;color:#fff;font:italic 400 5.8px/1.75 'Lato',sans-serif"><span style="color:#6aa6e8;font-size:9px">“</span> Liquorice candy drops applicake apple pie cupcake brownie bear claw cake ginger bread cotton candy. Bear claw croissant apple pie. Croissant cake sweet puff wafer . Liquorice candy drops applicake <span style="color:#6aa6e8;font-size:9px">”</span></p>
  <div class="page">02</div>
</section>

<!-- 4 Section divider -->
<section class="slide c1 r2" style="background:var(--red)">
  <div class="ph" role="img" aria-label="Business person touching a screen, red tinted" style="left:0;top:0;width:384px;height:220px;background:radial-gradient(ellipse at 45% 40%,#d8374a,#b50c1f 55%,#a30818)"></div>
  <div class="brand light"><span class="mark"></span><span>Copperline<br>Ventures</span></div>
  <h2 style="position:absolute;left:0;width:384px;top:81px;text-align:center;color:#fff;font:900 17px/1 'Lato',sans-serif">SECTION DIVIDER HERE</h2>
  <p class="copy white" style="left:48px;top:105px;width:288px;text-align:center;font-size:5px">Liquorice candy drops applicake apple pie cupcake brownie bear claw cake gingerbread cotton candy. Bear claw croissant apple pie. Croissant cake sweet puff wafer . Liquorice candy drops applicake apple pie cupcake brownie bear claw</p>
  <div class="page">02</div>
</section>

<!-- 5 Our products (image left) -->
<section class="slide c2 r2">
  <div class="ph" role="img" aria-label="Cloud computing icons on red background" style="left:0;top:0;width:213px;height:220px;background:linear-gradient(160deg,#d2465a,#b8192c 60%,#a60d1e)"></div>
  <div class="ph" role="img" aria-label="Hand touching a cloud screen" style="left:22px;top:68px;width:178px;height:73px;background:linear-gradient(135deg,#c7cbd0,#6f7983 60%,#4a535c);border:1px solid #fff"></div>
  <div class="brand"><span class="mark"></span><span>Copperline<br>Ventures</span></div>
  <h2 style="position:absolute;left:234px;top:50px;color:var(--red);font:300 12px/1 'Lato',sans-serif">OUR PRODUCTS</h2>
  <p class="copy justify" style="left:234px;top:68px;width:130px;line-height:2.1">Liquorice candy drops applicake apple pie cupcake brownie bear claw cake gingerbread cotton candy. Bear claw croissant apple pie. Croissant cake sweet puff wafer . Liquorice candy drops applicake apple pie cupcake brownie bear claw cake gingerbread cotton candy. Bear claw croissant apple pie. Croissant cake sweet puff wafer. Liquorice candy drops applicake apple pie cupcake brownie bear claw cake gingerbread cotton candy.</p>
  <div class="page">01</div>
</section>

<!-- 6 Feature image with caption -->
<section class="slide c3 r2">
  <div class="ph" role="img" aria-label="Data centre server aisle lit in blue" style="left:0;top:0;width:216px;height:164px;background:linear-gradient(90deg,#1c2a8a,#5a78e6 45%,#c3d4ff 52%,#4d66d8 60%,#16207a)"></div>
  <div style="position:absolute;left:0;top:164px;width:216px;height:56px;background:var(--red)"></div>
  <p class="copy white" style="left:12px;top:172px;width:196px">Liquorice candy drops applicake apple pie cupcake brownie bear claw cake gingerbread cotton candy. Liquorice candy drops applicake apple pie cupcake brownie bear claw cake gingerbread cotton candy.</p>
  <div class="brand"><span class="mark"></span><span>Copperline<br>Ventures</span></div>
  <p class="copy justify" style="left:236px;top:56px;width:130px;font-size:5.6px;line-height:2">Liquorice candy drops applicake apple pie cupcake brownie bear claw cake gingerbread cotton candy. Bear claw croissant apple pie. Croissant cake sweet puff wafer . Liquorice candy drops applicake apple pie cupcake brownie bear claw cake gingerbread cotton candy. Bear claw croissant apple pie. Croissant cake sweet puff wafer. Liquorice candy drops applicake apple pie cupcake brownie bear claw cake gingerbread cotton candy.</p>
  <div class="page">01</div>
</section>

<!-- 7 Main title with numbered sections -->
<section class="slide c1 r3">
  <h2 class="head bar" style="font-size:8.5px">Main Title Here</h2>
  <div class="brand"><span class="mark"></span><span>Copperline<br>Ventures</span></div>
  <div style="position:absolute;left:84px;top:76px;width:282px;height:1px;background:#e4e4e4"></div>
  <div style="position:absolute;left:84px;top:132px;width:282px;height:1px;background:#e4e4e4"></div>
  <div style="position:absolute;left:128px;top:44px;width:1px;height:160px;background:#e4e4e4"></div>
  <h3 class="sub head under" style="left:19px;top:48px;font-size:7.6px;text-transform:none">Section Title Here</h3>
  <h3 class="sub head under" style="left:19px;top:102px;font-size:7.6px;text-transform:none">Section Title Here</h3>
  <h3 class="sub head under" style="left:19px;top:158px;font-size:7.6px;text-transform:none">Section Title Here</h3>
  <span style="position:absolute;left:82px;top:50px;color:var(--pink);font:700 34px/1 'Lato',sans-serif">01</span>
  <span style="position:absolute;left:82px;top:104px;color:var(--pink);font:700 34px/1 'Lato',sans-serif">02</span>
  <span style="position:absolute;left:82px;top:160px;color:var(--pink);font:700 34px/1 'Lato',sans-serif">03</span>
  <p class="copy justify" style="left:137px;top:46px;width:240px">Liquorice candy drops applicake apple pie cupcake brownie bear claw cake gingerbread cotton candy. Bear claw croissant apple pie. Croissant cake sweet puff wafer . Liquorice candy drops applicake apple pie cupcake brownie bear claw cake gingerbread cotton candy. Bear claw croissant apple pie. Croissant cake sweet puff wafer.</p>
  <p class="copy justify" style="left:137px;top:100px;width:240px">Liquorice candy drops applicake apple pie cupcake brownie bear claw cake gingerbread cotton candy. Bear claw croissant apple pie. Croissant cake sweet puff wafer . Liquorice candy drops applicake apple pie cupcake brownie bear claw cake gingerbread cotton candy. Bear claw croissant apple pie. Croissant cake sweet puff wafer.</p>
  <p class="copy justify" style="left:137px;top:156px;width:240px">Liquorice candy drops applicake apple pie cupcake brownie bear claw cake gingerbread cotton candy. Bear claw croissant apple pie. Croissant cake sweet puff wafer . Liquorice candy drops applicake apple pie cupcake brownie bear claw cake gingerbread cotton candy. Bear claw croissant apple pie. Croissant cake sweet puff wafer.</p>
  <div class="page">01</div>
</section>

<!-- 8 Our products, numbered bars -->
<section class="slide c2 r3">
  <h2 class="head bar">Our Products</h2>
  <div class="brand"><span class="mark"></span><span>Copperline<br>Ventures</span></div>
  <div style="position:absolute;left:0;top:42px;width:122px;height:43px;background:var(--red)"></div>
  <div style="position:absolute;left:0;top:98px;width:122px;height:43px;background:var(--red)"></div>
  <div style="position:absolute;left:0;top:154px;width:122px;height:43px;background:var(--red)"></div>
  <span style="position:absolute;left:81px;top:51px;color:rgba(255,255,255,.35);font:700 34px/1 'Lato',sans-serif">01</span>
  <span style="position:absolute;left:81px;top:107px;color:rgba(255,255,255,.35);font:700 34px/1 'Lato',sans-serif">02</span>
  <span style="position:absolute;left:81px;top:163px;color:rgba(255,255,255,.35);font:700 34px/1 'Lato',sans-serif">03</span>
  <div style="position:absolute;left:128px;top:44px;width:1px;height:160px;background:#e4e4e4"></div>
  <p class="copy justify" style="left:137px;top:46px;width:240px">Liquorice candy drops applicake apple pie cupcake brownie bear claw cake gingerbread cotton candy. Bear claw croissant apple pie. Croissant cake sweet puff wafer . Liquorice candy drops applicake apple pie cupcake brownie bear claw cake gingerbread cotton candy. Bear claw croissant apple pie. Croissant cake sweet puff wafer.</p>
  <p class="copy justify" style="left:137px;top:100px;width:240px">Liquorice candy drops applicake apple pie cupcake brownie bear claw cake gingerbread cotton candy. Bear claw croissant apple pie. Croissant cake sweet puff wafer . Liquorice candy drops applicake apple pie cupcake brownie bear claw cake gingerbread cotton candy. Bear claw croissant apple pie. Croissant cake sweet puff wafer.</p>
  <p class="copy justify" style="left:137px;top:156px;width:240px">Liquorice candy drops applicake apple pie cupcake brownie bear claw cake gingerbread cotton candy. Bear claw croissant apple pie. Croissant cake sweet puff wafer . Liquorice candy drops applicake apple pie cupcake brownie bear claw cake gingerbread cotton candy. Bear claw croissant apple pie. Croissant cake sweet puff wafer.</p>
  <div class="page">01</div>
</section>

<!-- 9 Our services with image circles -->
<section class="slide c3 r3">
  <h2 class="head bar">Our Services</h2>
  <div class="brand"><span class="mark"></span><span>Copperline<br>Ventures</span></div>
  <h3 class="sub" style="left:20px;top:47px">Product Subtext Here</h3>
  <p class="copy" style="left:20px;top:56px;width:245px">Liquorice candy drops applicake apple pie cupcake brownie bear claw cake gingerbread cotton candy. Bear claw croissant apple pie. Croissant cake sweet puff wafer . Liquorice candy drops applicake apple pie cupcake brownie bear claw cake gingerbread cotton candy. Bear claw croissant apple pie. Croissant cake sweet puff wafer. Liquorice candy drops applicake apple pie cupcake brownie bear claw cake gingerbread cotton candy. Bear claw croissant apple pie. Croissant cake sweet puff wafer.</p>
  <h3 class="sub" style="left:20px;top:125px">Product Subtext Here</h3>
  <p class="copy" style="left:20px;top:134px;width:245px">Liquorice candy drops applicake apple pie cupcake brownie bear claw cake gingerbread cotton candy. Bear claw croissant apple pie. Croissant cake sweet puff wafer . Liquorice candy drops applicake apple pie cupcake brownie bear claw cake gingerbread cotton candy. Bear claw croissant apple pie. Croissant cake sweet puff wafer. Liquorice candy drops applicake apple pie cupcake brownie bear claw cake gingerbread cotton candy. Bear claw croissant apple pie. Croissant cake sweet puff wafer.</p>
  <div style="position:absolute;left:286px;top:44px;width:67px;height:67px;border-radius:50%;background:var(--red);color:#fff;font:700 8.5px/1.2 'Lato',sans-serif;display:flex;align-items:center;justify-content:center;text-align:center">IMAGE<br>HERE</div>
  <div style="position:absolute;left:286px;top:127px;width:67px;height:67px;border-radius:50%;background:var(--red);color:#fff;font:700 8.5px/1.2 'Lato',sans-serif;display:flex;align-items:center;justify-content:center;text-align:center">IMAGE<br>HERE</div>
  <div class="page">01</div>
</section>

<!-- 10 Logo section -->
<section class="slide c1 r4">
  <h2 class="head bar" style="font-size:8.5px">Logo Section here</h2>
  <div class="brand"><span class="mark"></span><span>Copperline<br>Ventures</span></div>
  <div class="ph" role="img" aria-label="Partner logo placeholder" style="left:27px;top:50px;width:34px;height:30px;background:#8d8d8d;border-radius:4px"></div>
  <div class="ph" role="img" aria-label="Partner logo placeholder" style="left:27px;top:105px;width:34px;height:30px;background:#8d8d8d;border-radius:4px"></div>
  <div class="ph" role="img" aria-label="Partner logo placeholder" style="left:20px;top:162px;width:52px;height:20px;background:#8d8d8d;border-radius:4px"></div>
  <p class="copy" style="left:84px;top:50px;width:132px">Liquorice candy drops applicake apple pie cupcake brownie bear claw cake gingerbread cotton candy. Bear claw croissant apple pie. Croissant cake sweet puff wafer .</p>
  <p class="copy" style="left:84px;top:104px;width:132px">Liquorice candy drops applicake apple pie cupcake brownie bear claw cake gingerbread cotton candy. Bear claw croissant apple pie. Croissant cake sweet puff wafer .</p>
  <p class="copy" style="left:84px;top:158px;width:132px">Liquorice candy drops applicake apple pie cupcake brownie bear claw cake gingerbread cotton candy. Bear claw croissant apple pie. Croissant cake sweet puff wafer .</p>
  <div style="position:absolute;left:222px;top:48px;width:1px;height:150px;background:#e4e4e4"></div>
  <p class="copy justify" style="left:232px;top:48px;width:144px;line-height:2">Liquorice candy drops applicake apple pie cupcake brownie bear claw cake gingerbread cotton candy. Bear claw croissant apple pie. Croissant cake sweet puff wafer . Liquorice candy drops applicake apple pie cupcake brownie bear claw cake gingerbread cotton candy. Bear claw croissant apple pie. Croissant cake sweet puff wafer .</p>
  <p class="copy justify" style="left:232px;top:121px;width:144px;line-height:2">Liquorice candy drops applicake apple pie cupcake brownie bear claw cake gingerbread cotton candy. Bear claw croissant apple pie. Croissant cake sweet puff wafer . Liquorice candy drops applicake apple pie cupcake brownie bear claw cake gingerbread cotton candy. Bear claw croissant apple pie. Croissant cake sweet puff wafer .</p>
  <div class="page">01</div>
</section>

<!-- 11 Our products mosaic -->
<section class="slide c2 r4">
  <h2 class="head bar">Our Products</h2>
  <div class="brand"><span class="mark"></span><span>Copperline<br>Ventures</span></div>
  <div style="position:absolute;left:100px;top:38px;width:1px;height:182px;background:var(--red)"></div>
  <div style="position:absolute;left:0;top:63px;width:100px;height:66px;background:#c9c9c9"></div>
  <p style="position:absolute;left:8px;top:78px;width:88px;color:var(--red);font:400 4.8px/1.75 'Lato',sans-serif">Liquorice candy drops applicake apple pie cupcake brownie bear claw cake gingerbread cotton candy. Bear claw croissant apple pie. Croissant cake sweet puff wafer . pie. Croissant cake sweet puff wafer.</p>
  <div class="ph" role="img" aria-label="Hands holding a cloud symbol" style="left:101px;top:63px;width:99px;height:66px;background:linear-gradient(135deg,#3e4c5e,#7f98ad 55%,#2d3846)"></div>
  <span style="position:absolute;left:56px;top:150px;color:var(--pink);font:700 34px/1 'Lato',sans-serif">03</span>
  <p class="copy justify" style="left:110px;top:150px;width:84px">Liquorice candy drops applicake apple pie cupcake brownie bear claw cake gingerbread cotton candy. Bear claw croissant apple pie. Croissant cake sweet</p>
  <div style="position:absolute;left:200px;top:34px;width:77px;height:186px;background:var(--red)"></div>
  <div style="position:absolute;left:212px;top:62px;width:53px;height:53px;border-radius:50%;border:1px solid rgba(255,255,255,.6);color:#fff;font:400 10px/51px 'Lato',sans-serif;text-align:center">80%</div>
  <p class="copy white" style="left:205px;top:122px;width:67px;text-align:center">Liquorice candy drops applicake apple pie cupcake brownie bear claw cake gingerbread cotton candy.</p>
  <p class="copy white" style="left:205px;top:170px;width:67px;text-align:center">Bear claw croissant apple pie. Croissant cake sweet puff wafer . pie. Croissant cake sweet puff wafer.</p>
  <div class="ph" role="img" aria-label="Business person touching a cloud interface" style="left:277px;top:34px;width:107px;height:186px;background:linear-gradient(160deg,#6d7a88,#2f3a48 55%,#1e2632)"></div>
  <div class="page">01</div>
</section>

<!-- 12 Our services, two images -->
<section class="slide c3 r4">
  <h2 class="head bar">Our Services</h2>
  <div class="brand"><span class="mark"></span><span>Copperline<br>Ventures</span></div>
  <div class="ph" role="img" aria-label="Hands holding a cloud, round image" style="left:56px;top:36px;width:82px;height:82px;border-radius:50%;background:radial-gradient(circle at 40% 40%,#9fb6cf,#2f4154 70%)"></div>
  <div class="ph" role="img" aria-label="Hands holding a cloud, round image" style="left:219px;top:36px;width:82px;height:82px;border-radius:50%;background:radial-gradient(circle at 50% 45%,#bcd0e6,#263444 70%)"></div>
  <h3 class="sub" style="left:0;width:194px;top:135px;text-align:center">Product Subtext Here</h3>
  <h3 class="sub" style="left:166px;width:196px;top:135px;text-align:center">Product Subtext Here</h3>
  <p class="copy" style="left:16px;top:144px;width:160px;text-align:center">Liquorice candy drops applicake apple pie cupcake brownie bear claw cake gingerbread cotton candy. Bear claw croissant apple pie. Croissant cake sweet puff wafer . Liquorice candy drops applicake apple pie cupcake brownie bear claw cake gingerbread cotton candy.</p>
  <p class="copy" style="left:188px;top:144px;width:160px;text-align:center">Liquorice candy drops applicake apple pie cupcake brownie bear claw cake gingerbread cotton candy. Bear claw croissant apple pie. Croissant cake sweet puff wafer . Liquorice candy drops applicake apple pie cupcake brownie bear claw cake gingerbread cotton candy.</p>
  <div class="page">01</div>
</section>

<!-- 13 Our products, stat panel -->
<section class="slide c1 r5">
  <h2 class="head bar">Our Products</h2>
  <div class="brand"><span class="mark"></span><span>Copperline<br>Ventures</span></div>
  <div class="ph" role="img" aria-label="Businessman holding a glowing cloud" style="left:0;top:38px;width:126px;height:182px;background:linear-gradient(160deg,#8aa4bf,#2f4766 50%,#1a2535)"></div>
  <div style="position:absolute;left:126px;top:38px;width:151px;height:182px;background:var(--red)"></div>
  <div style="position:absolute;left:180px;top:64px;width:47px;height:47px;border-radius:50%;border:1px solid rgba(255,255,255,.6);color:#fff;font:400 10px/45px 'Lato',sans-serif;text-align:center">80%</div>
  <p class="copy white" style="left:148px;top:124px;width:118px">Liquorice candy drops applicake apple pie cupcake brownie bear claw cake gingerbread cotton candy.</p>
  <p class="copy white" style="left:148px;top:148px;width:118px">Bear claw croissant apple pie. Croissant cake sweet puff wafer . pie. Croissant cake sweet puff wafer.</p>
  <p class="copy white" style="left:148px;top:172px;width:118px">Bear claw croissant apple pie. Croissant cake sweet puff wafer . pie. Croissant cake sweet puff wafer.</p>
  <div class="ph" role="img" aria-label="Business person touching a cloud interface" style="left:277px;top:38px;width:107px;height:182px;background:linear-gradient(160deg,#6d7a88,#2f3a48 55%,#1e2632)"></div>
  <div class="page">01</div>
</section>

<!-- 14 Our demo, device -->
<section class="slide c2 r5">
  <h2 class="head bar">Our Demo</h2>
  <div class="brand"><span class="mark"></span><span>Copperline<br>Ventures</span></div>
  <p class="copy" style="left:17px;top:55px;width:124px">Liquorice candy drops applicake apple pie cupcake brownie bear claw cake gingerbread cotton candy. Bear claw croissant apple pie. Croissant cake sweet puff wafer .</p>
  <p class="copy" style="left:17px;top:105px;width:124px">Liquorice candy drops applicake apple pie cupcake brownie bear claw cake gingerbread cotton candy. Bear claw croissant apple pie. Croissant cake sweet puff wafer . Liquorice candy drops applicake apple pie cupcake brownie bear claw cake gingerbread cotton candy. Bear claw croissant apple pie. Croissant cake sweet puff wafer . Liquorice candy drops applicake apple pie cupcake brownie bear claw cake gingerbread cotton candy. Bear claw croissant apple pie. Croissant cake sweet puff wafer .</p>
  <div class="ph" role="img" aria-label="Smartphone showing a colourful app interface" style="left:152px;top:45px;width:76px;height:157px;border-radius:7px;background:#1c1c1c;padding:13px 6px 18px">
    <div style="width:100%;height:100%;background:linear-gradient(180deg,#1e8fe0 0 55%,#e8a21a 55% 100%)"></div>
  </div>
  <p class="copy" style="left:240px;top:55px;width:128px">Liquorice candy drops applicake apple pie cupcake brownie bear claw cake gingerbread cotton candy. Bear claw croissant apple pie. Croissant cake sweet puff wafer .</p>
  <p class="copy" style="left:240px;top:100px;width:128px">Liquorice candy drops applicake apple pie cupcake brownie bear claw cake gingerbread cotton candy. Bear claw croissant apple pie. Croissant cake sweet puff wafer .</p>
  <p class="copy" style="left:240px;top:152px;width:128px">Liquorice candy drops applicake apple pie cupcake brownie bear claw cake gingerbread cotton candy. Bear claw croissant apple pie. Croissant cake sweet puff wafer .</p>
  <div class="page">01</div>
</section>

<!-- 15 Our demo, table -->
<section class="slide c3 r5">
  <h2 class="head bar">Our Demo</h2>
  <div class="brand"><span class="mark"></span><span>Copperline<br>Ventures</span></div>
  <table style="position:absolute;left:10px;top:46px;width:364px;border-collapse:collapse;font-family:'Lato',sans-serif">
    <thead>
      <tr style="background:var(--red);color:#fff;font:700 6.4px/1 'Lato',sans-serif;text-align:left">
        <th style="width:70px;height:18px;padding-left:16px">SECTION</th>
        <th style="padding-left:10px">MAIN TITLE HERE</th>
      </tr>
    </thead>
    <tbody style="font-size:4.6px;color:var(--grey)">
      <tr style="height:25px;background:#ececec"><td style="color:var(--red);font-size:6px;padding-left:20px;border-right:1px solid #fff">ICON - 1</td><td style="padding:0 10px;line-height:1.8">Liquorice candy drops applicake apple pie cupcake brownie bear claw cake gingerbread cotton candy. Bear claw croissant apple pie. Croissant cake sweet puff wafer . Liquorice candy drops applicake apple pie</td></tr>
      <tr style="height:25px;background:#f9f9f9"><td style="color:var(--red);font-size:6px;padding-left:20px;border-right:1px solid #e6e6e6">ICON - 1</td><td style="padding:0 10px;line-height:1.8">Liquorice candy drops applicake apple pie cupcake brownie bear claw cake gingerbread cotton candy. Bear claw croissant apple pie. Croissant cake sweet puff wafer . Liquorice candy drops applicake apple pie</td></tr>
      <tr style="height:25px;background:#ececec"><td style="color:var(--red);font-size:6px;padding-left:20px;border-right:1px solid #fff">ICON - 1</td><td style="padding:0 10px;line-height:1.8">Liquorice candy drops applicake apple pie cupcake brownie bear claw cake gingerbread cotton candy. Bear claw croissant apple pie. Croissant cake sweet puff wafer . Liquorice candy drops applicake apple pie</td></tr>
      <tr style="height:25px;background:#f9f9f9"><td style="color:var(--red);font-size:6px;padding-left:20px;border-right:1px solid #e6e6e6">ICON - 1</td><td style="padding:0 10px;line-height:1.8">Liquorice candy drops applicake apple pie cupcake brownie bear claw cake gingerbread cotton candy. Bear claw croissant apple pie. Croissant cake sweet puff wafer . Liquorice candy drops applicake apple pie</td></tr>
      <tr style="height:25px;background:#ececec"><td style="color:var(--red);font-size:6px;padding-left:20px;border-right:1px solid #fff">ICON - 1</td><td style="padding:0 10px;line-height:1.8">Liquorice candy drops applicake apple pie cupcake brownie bear claw cake gingerbread cotton candy. Bear claw croissant apple pie. Croissant cake sweet puff wafer . Liquorice candy drops applicake apple pie</td></tr>
    </tbody>
  </table>
  <div class="page">01</div>
</section>

</body>
</html>
```